Bath Salt - Sachet Packet (5 Scents) Packaging Design

We sell products to professional salons in the USA. This product is used as the first step when treating clients to a pedicure spa. This product is called SALT SOAK (or Bath Salts). The salt is added to the water to cleanse the skin, create a pleasant fragrance, and change the color of the water.

This product has 5 different variations, based on the scent of the salt soak. The available scents are:
LAVENDER, MANDARIN, CUCUMBER-MELON, JASMINE, MINT.

We would like to see package designs for all 5 scents. The theme should be consistent across the different variations of scents. The design should focus on bright, attractive, floral colors/themes. The design should fully express the color and imagery that are associated with each scent. (Lavender scent should include purple colors, lavender flower, etc.). See example images for reference of popular designs/brands.

Ideal designs will incorporate a luxurious and premium aesthetic that combines elegant imagery, colors, and premium finishes. See example images for reference of popular designs/brands.

Each packet is individually sealed. See dimension artwork file for reference of the sachet packet size and layout.

See the attached document guidelines for more information about product name, key text, and brand logo.

Target Market(s)

Beauty & Nail Salons

Industry/Entity Type

Beauty

Font styles to use
Sans Serif
Script

Requirements
Must have
• Bright imagery and colors that relate to the target fragrance
Nice to have
• Premium and luxurious finishes (shiny accent, etc.)

```html
<!DOCTYPE html>
<html lang="en">
<head>
<meta charset="utf-8">
<title>LUMEA Sea Salt Soak – Lavender Sachet</title>
<link href="https://fonts.googleapis.com/css2?family=Lato:wght@300;400;700&family=Libre+Baskerville:wght@700&display=swap" rel="stylesheet">
<style>
  :root {
    --backdrop: #4b4b4d;
    --lilac-pale: #efeaf8;
    --lilac-soft: #d9cdef;
    --lilac-mid: #b9a6e0;
    --lavender: #8c6cc8;
    --purple: #6f3fb0;
    --purple-deep: #5a2a98;
    --ink: #231f20;
    --white: #ffffff;
    --stone: #d9d6cc;
  }
  * { margin: 0; padding: 0; box-sizing: border-box; }
  html, body { width: 1200px; height: 951px; overflow: hidden; }
  body {
    background: var(--backdrop);
    font-family: "Lato", sans-serif;
    position: relative;
  }
  .sachet {
    position: absolute;
    top: 183px;
    width: 420px;
    height: 627px;
    clip-path: polygon(2% 0, 98% 0, 100% 3%, 100% 12%, 94% 97%, 90% 100%, 10% 100%, 6% 97%, 0 12%, 0 3%);
    overflow: hidden;
  }
  .sachet--front { left: 154px; }
  .sachet--back { left: 619px; }
  .marble {
    position: absolute; inset: 0;
    background:
      radial-gradient(ellipse 60% 30% at 25% 20%, var(--lilac-soft), transparent 70%),
      radial-gradient(ellipse 50% 40% at 80% 55%, var(--lilac-soft), transparent 70%),
      radial-gradient(ellipse 40% 30% at 20% 75%, var(--lilac-mid), transparent 70%),
      linear-gradient(160deg, var(--lilac-pale), var(--white) 45%, var(--lilac-pale));
  }
  .band {
    position: absolute; left: 0; right: 0; bottom: 0; height: 70px;
    background: linear-gradient(180deg, var(--purple), var(--purple-deep));
  }
  .centered { position: absolute; left: 0; right: 0; text-align: center; z-index: 2; }
  .brand {
    font-weight: 400; font-size: 42px; color: var(--ink);
    letter-spacing: 1px; line-height: 1;
    display: flex; align-items: center; justify-content: center; gap: 8px;
  }
  .brand-dot { width: 9px; height: 9px; border-radius: 50%; background: var(--ink); }
  .brand-tag { font-size: 6px; letter-spacing: 3px; color: #777; }
  .product-line { font-weight: 300; font-size: 19px; color: var(--purple); letter-spacing: .5px; }
  .badge-circle {
    position: absolute; left: 116px; top: 212px; width: 184px; height: 184px;
    border-radius: 50%; background: var(--lilac-soft); z-index: 1;
  }
  .kicker { font-weight: 400; font-size: 13px; color: var(--lavender); letter-spacing: 1px; }
  .scent { font-family: "Libre Baskerville", serif; font-weight: 700; font-size: 24px; color: var(--purple); letter-spacing: 1.5px; }
  .variant { font-weight: 400; font-size: 11px; color: var(--lavender); letter-spacing: 1.5px; }
  .art { position: absolute; z-index: 1; }
  .art--flowers {
    left: 78px; top: 342px; width: 140px; height: 90px; border-radius: 50%;
    background: radial-gradient(ellipse at 45% 45%, var(--purple), var(--lavender) 60%, transparent 72%);
  }
  .art--spa {
    background: linear-gradient(180deg, rgba(140,108,200,.55), rgba(185,166,224,.5) 55%, var(--stone));
    border-radius: 40px 40px 8px 8px;
  }
  .claims { position: absolute; font-size: 8.5px; font-weight: 400; color: var(--purple); line-height: 1.4; z-index: 2; }
  .claims li { list-style: none; }
  .claims li::before { content: "• "; }
  .free-from { position: absolute; left: 187px; top: 500px; font-size: 8.5px; color: var(--purple); font-weight: 400; z-index: 2; }
  .free-from strong { font-size: 12px; font-weight: 400; }
  .cert-mark { position: absolute; width: 26px; height: 26px; border: 1px solid var(--white); border-radius: 50%; bottom: 22px; z-index: 2; }
  .net-weight { position: absolute; right: 56px; bottom: 24px; font-family: "Libre Baskerville", serif; font-size: 18px; color: var(--white); z-index: 2; }
  .info { font-size: 9.3px; color: var(--purple-deep); line-height: 1.15; }
  .info h3 { font-size: 9.3px; font-weight: 400; color: var(--lavender); letter-spacing: .3px; }
  .info p { margin-top: 2px; }
  .directions { top: 210px; }
  .ingredients { top: 268px; }
  .caution { top: 337px; }
  .caution p { margin-top: 4px; }
  .distributor { position: absolute; left: 211px; top: 487px; font-size: 9.3px; color: var(--purple-deep); line-height: 1.35; z-index: 2; }
  .distributor h3 { font-size: 9.3px; font-weight: 400; color: var(--lavender); }
  .origin { position: absolute; left: 211px; top: 544px; font-size: 10px; font-weight: 300; color: var(--purple); display: flex; gap: 6px; align-items: center; z-index: 2; }
  .origin span.mark { width: 12px; height: 12px; border-radius: 50%; background: var(--lavender); display: inline-block; }
</style>
</head>
<body>

<section class="sachet sachet--front">
  <div class="marble" role="img" aria-label="Lilac and white marbled pattern with thin gold veins"></div>
  <div class="band"></div>

  <div class="centered brand" style="top:110px;">LUMEA<span class="brand-dot"></span></div>
  <div class="centered brand-tag" style="top:154px;">BEAUTY &amp; SPA</div>
  <div class="centered product-line" style="top:172px;">SEA SALT SOAK</div>

  <div class="badge-circle"></div>
  <div class="centered kicker" style="top:271px;">PREMIUM</div>
  <div class="centered scent" style="top:289px;">LAVENDER</div>
  <div class="centered variant" style="top:322px;">DELUXE PEDICURE</div>

  <div class="art art--flowers" role="img" aria-label="Illustration of purple violet flowers with golden leaf sprigs"></div>
  <div class="art art--spa" style="left:52px; top:440px; width:125px; height:125px;" role="img" aria-label="Illustration of lavender stems, stacked spa stones and a glass bowl of purple bath salt"></div>

  <ul class="claims" style="left:187px; top:477px;">
    <li>Single-Use.</li>
    <li>Sealed Fresh.</li>
  </ul>
  <ul class="claims" style="left:274px; top:473px;">
    <li>Made with Eco Cert.</li>
    <li>Organic Ingredients.</li>
  </ul>
  <div class="free-from"><strong>NO</strong> Triclosan, Animal Products, Sulfates.</div>

  <span class="cert-mark" style="left:48px;"></span>
  <span class="cert-mark" style="left:82px;"></span>
  <div class="net-weight">25g</div>
</section>

<section class="sachet sachet--back">
  <div class="marble" role="img" aria-label="Lilac and white marbled pattern"></div>
  <div class="band"></div>

  <div class="centered brand" style="top:46px;">LUMEA<span class="brand-dot"></span></div>
  <div class="centered brand-tag" style="top:90px; left:60px;">BEAUTY &amp; SPA</div>
  <div class="centered product-line" style="top:122px;">SEA SALT SOAK</div>
  <div class="centered scent" style="top:154px; font-size:16px;">LAVENDER</div>
  <div class="centered variant" style="top:175px; font-size:9.5px;">DELUXE PEDICURE</div>

  <div class="centered info directions">
    <h3>DIRECTIONS:</h3>
    <p>Add desired amount to warm water,<br>soak feet, and then rinse.</p>
  </div>
  <div class="centered info ingredients">
    <h3>INGREDIENTS:</h3>
    <p>Lorem ipsum dolor sit amet, consectetur<br>adipiscing elit, sed do eiusmod tempor incididunt<br>ut labore et dolore magna aliqua.</p>
  </div>
  <div class="centered info caution">
    <h3>CAUTION:</h3>
    <p>For external use only.</p>
    <p>Avoid use when skin is damaged or near any<br>open cuts, wounds, or irritations.</p>
    <p>If signs of irritation occur, stop use immediately<br>and consult a doctor.</p>
    <p>Keep away from direct sunlight.</p>
    <p>Store at room temperature and use<br>immediately after opening.</p>
    <p>Keep out of reach of children.</p>
  </div>

  <div class="art art--spa" style="left:62px; top:468px; width:115px; height:97px;" role="img" aria-label="Illustration of lavender stems, stacked spa stones and a glass bowl of purple bath salt"></div>

  <div class="distributor">
    <h3>DISTRIBUTED BY:</h3>
    Bright Harbor Supply, Inc.<br>
    Linden Falls, IN 46000<br>
    www.brightharborsupply.com
  </div>
  <div class="origin">MADE IN KOREA <span class="mark"></span><span class="mark"></span></div>
</section>

</body>
</html>
```